Seeking Talented PSD Designer for Real Estate Finance Web Site

Hello ...
Need a minimalist design for a high - end finance web site that conveys prestige / sophistication / class ... Below are comps for this project ...
http://www.tawnyridgefunding.com/
http://glenmoorfunds.com/
http://www.cedarloftfp.com/
http://halvornfunds.com/
Look forward too receiving proposals for this project ....
Target Market(s)
Commerciale entities seeking more than $500.0 k in interim capital ... These could include apartment owners / construction managers / restaurant owners / hotels / golf courses ...
Industry/Entity Type
Real Estate
Number of Pages Required
1 page
Requirements
Must have
- Super high quality graphic design ... Has to be marketable and convert customers to contact us ...
- Please refer to logo concept four ....
Should not have
- clunky / poor fonts /

```html
<!DOCTYPE html>
<html lang="en">
<head>
<meta charset="utf-8">
<title>Ashgrove Capital</title>
<link rel="stylesheet" href="https://fonts.googleapis.com/css2?family=Open+Sans:wght@400;600;700&family=Oswald:wght@300;400;500&family=Roboto+Condensed:wght@400&display=swap">
<style>
:root{
  --navy:#2e3f6b;
  --navy-deep:#26355c;
  --brand:#4a62a8;
  --ink:#555;
  --ink-dark:#333;
  --light:#f4f4f4;
  --footer:#232323;
  --white:#fff;
}
*{box-sizing:border-box;margin:0;padding:0}
html,body{width:1200px;height:2804px;overflow:hidden}
body{position:relative;font-family:"Open Sans",Arial,sans-serif;color:var(--ink);background:var(--white)}
.abs{position:absolute}
.hero{left:0;top:0;width:1200px;height:720px;background:linear-gradient(180deg,#3a3630 0%,#2a2d33 45%,#1c1f24 100%)}
.nav{left:0;top:0;width:1200px;height:62px;background:var(--navy);display:flex;justify-content:center;gap:56px;align-items:center;font-family:"Roboto Condensed",Arial,sans-serif;font-size:20px;color:var(--white);letter-spacing:.5px}
.brand-mark{left:536px;top:126px;width:128px;height:128px;border-radius:50%;background:#c9cbd0}
.brand-name{left:0;top:286px;width:1200px;text-align:center;font-family:"Open Sans",Arial,sans-serif;font-weight:400;color:var(--brand);font-size:62px;letter-spacing:8px;line-height:1}
.brand-sub{left:0;top:358px;width:1200px;text-align:center;font-weight:400;color:var(--brand);font-size:24px;letter-spacing:9px;line-height:1}
.tagline{left:150px;top:444px;width:900px;text-align:center;color:var(--white);font-size:40px;line-height:56px;letter-spacing:1px}
.welcome-bg{left:0;top:720px;width:1200px;height:448px;background:linear-gradient(135deg,#f2f2f2,#e6e6e6)}
.welcome-title{left:78px;top:780px;font-size:40px;font-weight:400;color:#555;letter-spacing:.5px;line-height:54px}
.accent{color:var(--navy)}
.welcome-text{left:78px;top:862px;width:670px;font-size:14.5px;line-height:25px;color:#666}
.btn{display:flex;align-items:center;justify-content:center;border-radius:26px;background:var(--navy);color:var(--white);font-size:24px}
.read-more{left:78px;top:1068px;width:186px;height:52px;font-size:23px}
.call{left:810px;top:780px;width:312px;height:312px;border:2px solid var(--navy);border-radius:50%;text-align:center}
.call-label{left:0;top:126px;width:100%;font-family:"Oswald",Arial,sans-serif;font-weight:300;font-size:36px;line-height:48px;color:#333}
.call-num{left:0;top:180px;width:100%;font-family:"Oswald",Arial,sans-serif;font-weight:500;font-size:46px;line-height:60px;color:var(--navy)}
.band{left:0;top:1168px;width:1200px;height:124px;background:var(--navy)}
.band-text{left:80px;top:1178px;width:760px;font-size:38px;line-height:48px;color:var(--white)}
.loan-btn{left:856px;top:1204px;width:266px;height:50px;background:var(--white);color:var(--navy);font-size:23px}
.services{left:0;top:1292px;width:1200px;height:396px;background:linear-gradient(180deg,#e9ecef,#f3f4f5)}
.svc{top:1348px;width:340px;text-align:center}
.svc-icon{width:124px;height:124px;border-radius:50%;background:var(--navy);margin:0 auto;display:flex;align-items:center;justify-content:center}
.svc h2{margin-top:20px;font-size:32px;font-weight:400;color:var(--navy);letter-spacing:1px}
.svc p{margin-top:8px;font-size:15px;line-height:25px;color:#222;padding:0 10px}
.recent-title{left:0;top:1720px;width:1200px;text-align:center;font-size:40px;color:#555;font-weight:400}
.featured{left:77px;top:1803px;width:333px;height:207px;background:var(--navy);color:var(--white);text-align:center}
.featured .city{margin-top:46px;font-size:20px}
.featured .price{margin-top:10px;font-size:21px;font-weight:700}
.detail{margin:12px auto 0;width:138px;height:40px;background:var(--white);color:var(--navy);display:flex;align-items:center;justify-content:center;font-size:19px;border-radius:2px}
.outro{left:200px;top:2316px;width:800px;text-align:center;font-size:15px;line-height:25px;color:#666}
.login{left:486px;top:2380px;width:228px;height:52px;border-radius:3px;font-size:22px;gap:8px}
.footer{left:0;top:2490px;width:1200px;height:314px;background:var(--footer)}
.fcol{top:2510px;width:250px;color:var(--white)}
.fcol h3{font-size:24px;font-weight:400;margin-bottom:14px}
.links li{list-style:none;font-size:15px;line-height:31px}
.links li::before{content:"›";font-weight:700;margin-right:10px}
.fcol p{font-size:15px;line-height:24px}
.email-field{margin-top:12px;width:232px;height:36px;border:1px solid #ccc;font-size:14px;padding:8px}
.subscribe{margin-top:15px;width:130px;height:34px;background:var(--white);color:var(--navy);font-size:15px;font-weight:700;display:flex;align-items:center;justify-content:center}
.post{display:flex;gap:10px;margin-bottom:10px}
.dot{flex:none;width:26px;height:26px;border-radius:50%;background:#777}
.post b{font-size:13px;color:#ccc}
.post span{display:block;font-size:13px;line-height:20px;color:#aaa}
.contact-row{display:flex;gap:12px;font-size:14px;line-height:22px;margin-bottom:10px}
.social{display:flex;gap:22px;margin-top:12px}
.social i{width:52px;height:52px;border-radius:50%;border:2px solid #bbb}
.social i:first-child{background:var(--white);border-color:var(--white)}
.copy{left:0;top:2764px;width:1200px;text-align:center;font-size:14px;color:#ddd;border-top:1px solid #3a3a3a;padding-top:10px}
</style>
</head>
<body>
<header class="abs hero" role="img" aria-label="Dusk skyline of a dense city of tall office towers"></header>
<nav class="abs nav"><span>HOME</span><span>ABOUT</span><span>SERVICES</span><span>TRANSACTIONS</span><span>NEWS</span><span>CONTACT</span></nav>
<div class="abs brand-mark"></div>
<div class="abs brand-name">ASHGROVE</div>
<div class="abs brand-sub">CAPITAL</div>
<p class="abs tagline">A SMART ALTERNATIVE TO CONVENTIONAL FINANCING</p>

<section class="abs welcome-bg" role="img" aria-label="White painted brick wall texture"></section>
<h1 class="abs welcome-title">WELCOME TO <span class="accent">ASHGROVE CAPITAL</span></h1>
<p class="abs welcome-text">Lorem Ipsum is simply dummy text of the printing and typesetting industry. Lorem Ipsum has been the industry's standard dummy text ever since the 1500s, when an unknown printer took a galley of type and scrambled it to make a type specimen book. It has survived not only five centuries, but also the leap into electronic typesetting, remaining essentially unchanged. It was popularised in the 1960s with the release of transfer sheets containing Lorem Ipsum passages, and more recently with layout software including versions of Lorem Ipsum.</p>
<div class="abs btn read-more">READ MORE</div>
<div class="abs call">
  <svg class="abs" style="left:136px;top:60px" width="40" height="48" viewBox="0 0 24 24"><path fill="#444" d="M6.6 10.8c1.4 2.8 3.8 5.1 6.6 6.6l2.2-2.2c.3-.3.7-.4 1-.2 1.1.4 2.3.6 3.6.6.6 0 1 .4 1 1V20c0 .6-.4 1-1 1C10.6 21 3 13.4 3 4c0-.6.4-1 1-1h3.5c.6 0 1 .4 1 1 0 1.3.2 2.5.6 3.6.1.3 0 .7-.2 1z"/></svg>
  <div class="abs call-label">CALL US ON</div>
  <div class="abs call-num">123 456 7890</div>
</div>

<section class="abs band"></section>
<p class="abs band-text">Lorem Ipsum is simply dummy text of the printing.</p>
<div class="abs btn loan-btn">LOAN APPLICATION</div>

<section class="abs services" role="img" aria-label="Faded pale city skyline with sunlight from the right"></section>
<div class="abs svc" style="left:67px">
  <div class="svc-icon"><svg width="64" height="56" viewBox="0 0 64 56"><path d="M32 6 14 22h6v14h24V22h6z" fill="#fff"/><path d="M4 40h18l14 6 24-10v6L36 54 4 48z" fill="#fff"/></svg></div>
  <h2>Loan Programs</h2>
  <p>Lorem Ipsum is simply dummy text of the printing and typesetting industry. Lorem Ipsum has been the industry.</p>
</div>
<div class="abs svc" style="left:431px">
  <div class="svc-icon"><svg width="60" height="64" viewBox="0 0 60 64" fill="none" stroke="#fff" stroke-width="4"><path d="M12 4v56M30 4v56M48 4v56"/><rect x="5" y="14" width="14" height="12" rx="3" fill="#2e3f6b"/><rect x="23" y="36" width="14" height="12" rx="3" fill="#2e3f6b"/><rect x="41" y="20" width="14" height="12" rx="3" fill="#2e3f6b"/></svg></div>
  <h2>Lending Parameters</h2>
  <p>Lorem Ipsum is simply dummy text of the printing and typesetting industry. Lorem Ipsum has been the industry.</p>
</div>
<div class="abs svc" style="left:796px">
  <div class="svc-icon"><svg width="64" height="60" viewBox="0 0 64 60" fill="#fff"><rect x="8" y="36" width="10" height="20"/><rect x="22" y="28" width="10" height="28"/><rect x="36" y="32" width="10" height="24"/><rect x="50" y="20" width="10" height="36"/><path d="M6 24 22 12l12 8L56 4" fill="none" stroke="#fff" stroke-width="4"/></svg></div>
  <h2>Investment Strategy</h2>
  <p>Lorem Ipsum is simply dummy text of the printing and typesetting industry. Lorem Ipsum has been the industry.</p>
</div>

<h2 class="abs recent-title">Recent <span class="accent">Transactions</span></h2>
<div class="abs featured"><div class="city">Corpus Christi, TX</div><div class="price">$1,925,000</div><div class="detail">View Detail</div></div>
<div class="abs" style="left:77px;top:2040px;width:333px;height:222px;background:linear-gradient(180deg,#7fb0e6,#b77b5e 55%,#6b8a3d)" role="img" aria-label="Brick apartment buildings with flower beds"></div>
<div class="abs" style="left:433px;top:1803px;width:333px;height:185px;background:linear-gradient(180deg,#6fa3d8,#e8eef0 50%,#6a7a5a)" role="img" aria-label="White office building with palm trees"></div>
<div class="abs" style="left:433px;top:2012px;width:333px;height:250px;background:linear-gradient(135deg,#b8c4cf,#4f78b4 60%,#e6e9ec)" role="img" aria-label="Curved glass facade of a modern building"></div>
<div class="abs" style="left:787px;top:1803px;width:333px;height:200px;background:linear-gradient(180deg,#3d7fd0,#d9d5cf 55%,#8a8f86)" role="img" aria-label="Modern apartment block with orange accents"></div>
<div class="abs" style="left:787px;top:2075px;width:333px;height:187px;background:linear-gradient(135deg,#cfdde9,#5a84b3 60%,#eaf0f5)" role="img" aria-label="Blue glass towers seen from below"></div>
<p class="abs outro">Lorem Ipsum is simply dummy text of the printing and typesetting industry. Lorem Ipsum has been the industry's standard dummy text ever since the 1500.</p>
<div class="abs btn login">Investor Login <svg width="16" height="18" viewBox="0 0 16 18"><path d="M4 8V5a4 4 0 0 1 8 0v3" fill="none" stroke="#fff" stroke-width="2"/><rect x="1" y="8" width="14" height="10" rx="1" fill="#fff"/></svg></div>

<footer class="abs footer"></footer>
<div class="abs fcol" style="left:78px">
  <h3>Useful Links</h3>
  <ul class="links"><li>Home</li><li>About</li><li>Services</li><li>Transactions</li><li>News</li><li>Contact</li></ul>
</div>
<div class="abs fcol" style="left:350px">
  <h3>Newsletter</h3>
  <p>Lorem Ipsum is simply dummy text of the printing.</p>
  <div class="email-field">Enter Email</div>
  <div class="subscribe">SUBSCRIBE</div>
</div>
<div class="abs fcol" style="left:622px">
  <h3>Social Feed</h3>
  <div class="post"><i class="dot"></i><div><b>@Renwick @Ashgrove Capital</b><span>Thank you very much!</span><span>4 days ago</span></div></div>
  <div class="post"><i class="dot"></i><div><b>@Renwick @Ashgrove Capital</b><span>Thank you very much!</span><span>4 days ago</span></div></div>
</div>
<div class="abs fcol" style="left:892px">
  <h3>Get In Touch</h3>
  <div class="contact-row"><svg width="14" height="20" viewBox="0 0 14 20"><path d="M7 0a7 7 0 0 0-7 7c0 5 7 13 7 13s7-8 7-13a7 7 0 0 0-7-7zm0 10a3 3 0 1 1 0-6 3 3 0 0 1 0 6z" fill="#fff"/></svg><span>Lorem Ipsum is simply dummy text of the printing.</span></div>
  <div class="contact-row"><svg width="16" height="16" viewBox="0 0 24 24"><path fill="#fff" d="M6.6 10.8c1.4 2.8 3.8 5.1 6.6 6.6l2.2-2.2c.3-.3.7-.4 1-.2 1.1.4 2.3.6 3.6.6.6 0 1 .4 1 1V20c0 .6-.4 1-1 1C10.6 21 3 13.4 3 4c0-.6.4-1 1-1h3.5c.6 0 1 .4 1 1 0 1.3.2 2.5.6 3.6.1.3 0 .7-.2 1z"/></svg><span>123 456 7890</span></div>
  <div class="contact-row"><svg width="18" height="14" viewBox="0 0 18 14"><rect x="1" y="1" width="16" height="12" fill="none" stroke="#fff" stroke-width="1.5"/><path d="M1 1l8 7 8-7" fill="none" stroke="#fff" stroke-width="1.5"/></svg><span>info@ashgrovecapital.com</span></div>
  <div class="social"><i></i><i></i><i></i></div>
</div>
<p class="abs copy">© <b>ASHGROVE CAPITAL</b> - 2016. All Rights Reserved.</p>
</body>
</html>
```